new business venture [ self employed ] will register my business name as " LEARNOVA "
what I will offer is :-
computer lessons for new beginners.
Initial set up and basic overview.
lessons per hour in the comfort of your own home.
special rates for customers aged 50+
First lesson is half price with no obligation for booking any further appointments.
a learning and training plan will be presented based on your requirements.
an appraisal update on your new skills.

contact info:-
0161 4972015
07700 918342
grenwick@vellumail.net

```html
<!DOCTYPE html>
<html lang="en">
<head>
<meta charset="utf-8">
<title>Learnova – Computer Lessons</title>
<link href="https://fonts.googleapis.com/css2?family=Federo&family=Saira+Condensed:wght@400;700&display=swap" rel="stylesheet">
<style>
  :root{
    --cyan-title:#1ff4f6;
    --cyan-tick:#14d8f2;
    --cyan-circle:#8cffff;
    --cyan-faint:#dcfbff;
    --blue-arc:#00b2ff;
    --ink:#141414;
    --white:#ffffff;
    --grey-dark:#6a6a6a;
    --grey-light:#f4f4f4;
  }
  html,body{margin:0;padding:0;overflow:hidden;background:var(--white);}
  .flyer{position:relative;width:1200px;height:851px;overflow:hidden;background:var(--white);font-family:"Saira Condensed",sans-serif;color:var(--ink);}
  .backdrop{position:absolute;inset:0;}
  .mascot-slot{position:absolute;left:129px;top:33px;width:286px;height:263px;border-radius:18px;
    background:radial-gradient(circle at 55% 45%,#4a4a4a 0%,#262626 55%,#d9d9d9 100%);opacity:.85;}
  .brand{position:absolute;left:420px;top:92px;margin:0;font-family:"Federo",sans-serif;font-weight:400;
    font-size:94px;line-height:1;letter-spacing:14px;color:var(--cyan-title);}
  .offer-list{position:absolute;left:425px;top:217px;margin:0;padding:0;list-style:none;width:620px;}
  .offer-list li{position:relative;padding-left:37px;font-size:25px;line-height:24px;margin-bottom:24px;letter-spacing:.6px;}
  .tick{position:absolute;left:3px;top:1px;width:23px;height:23px;}
  .contact{position:absolute;left:84px;top:627px;width:400px;text-align:center;}
  .contact-title{margin:0;font-weight:700;font-size:34px;line-height:38px;letter-spacing:.5px;}
  .contact-line{margin:0;font-size:36px;line-height:47px;letter-spacing:2px;}
</style>
</head>
<body>
<main class="flyer">
  <svg class="backdrop" width="1200" height="851" viewBox="0 0 1200 851" aria-hidden="true">
    <defs>
      <linearGradient id="steel" x1="0" y1="0" x2="1" y2="0">
        <stop offset="0" stop-color="var(--grey-dark)"/>
        <stop offset=".22" stop-color="var(--grey-light)"/>
        <stop offset=".75" stop-color="var(--grey-light)"/>
        <stop offset="1" stop-color="var(--grey-dark)"/>
      </linearGradient>
    </defs>
    <rect class="steel-frame" width="1200" height="851" fill="url(#steel)"/>
    <path class="sheet" d="M255 0 H1200 V20 C1130 300 900 700 570 851 H15 C40 600 120 300 255 0 Z" fill="var(--white)"/>
    <path class="sheet-edge-right" d="M1200 290 C1110 540 900 760 570 851" fill="none" stroke="var(--cyan-tick)" stroke-width="6"/>
    <path class="sheet-edge-left" d="M170 330 C100 450 50 650 20 851" fill="none" stroke="var(--cyan-circle)" stroke-width="10"/>
    <path class="sheet-arc" d="M720 0 C520 20 300 120 170 330" fill="none" stroke="var(--blue-arc)" stroke-width="8"/>
    <circle class="bubble" cx="323" cy="333" r="42" fill="var(--cyan-faint)"/>
    <circle class="bubble" cx="204" cy="473" r="76" fill="var(--cyan-faint)"/>
    <circle class="contact-disc" cx="286" cy="866" r="308" fill="var(--cyan-circle)"/>
  </svg>

  <div class="mascot-slot" role="img" aria-label="Cartoon computer mascot holding a pointer, with keyboard"></div>

  <h1 class="brand">LEARNOVA</h1>

  <ul class="offer-list">
    <li><svg class="tick" viewBox="0 0 24 24" aria-hidden="true"><circle cx="12" cy="12" r="12" fill="var(--cyan-tick)"/><path d="M6.5 12.5l3.5 3.5 7.5-7.5" fill="none" stroke="#fff" stroke-width="2.6"/></svg>Computer lessons for new beginners.</li>
    <li><svg class="tick" viewBox="0 0 24 24" aria-hidden="true"><circle cx="12" cy="12" r="12" fill="var(--cyan-tick)"/><path d="M6.5 12.5l3.5 3.5 7.5-7.5" fill="none" stroke="#fff" stroke-width="2.6"/></svg>Initial set up and basic overview.</li>
    <li><svg class="tick" viewBox="0 0 24 24" aria-hidden="true"><circle cx="12" cy="12" r="12" fill="var(--cyan-tick)"/><path d="M6.5 12.5l3.5 3.5 7.5-7.5" fill="none" stroke="#fff" stroke-width="2.6"/></svg>Lessons per hour in the comfort of your own home.</li>
    <li><svg class="tick" viewBox="0 0 24 24" aria-hidden="true"><circle cx="12" cy="12" r="12" fill="var(--cyan-tick)"/><path d="M6.5 12.5l3.5 3.5 7.5-7.5" fill="none" stroke="#fff" stroke-width="2.6"/></svg>Special rates for customers aged 50+</li>
    <li><svg class="tick" viewBox="0 0 24 24" aria-hidden="true"><circle cx="12" cy="12" r="12" fill="var(--cyan-tick)"/><path d="M6.5 12.5l3.5 3.5 7.5-7.5" fill="none" stroke="#fff" stroke-width="2.6"/></svg>First lesson is half price with no obligation for booking any<br>further appointments.</li>
    <li><svg class="tick" viewBox="0 0 24 24" aria-hidden="true"><circle cx="12" cy="12" r="12" fill="var(--cyan-tick)"/><path d="M6.5 12.5l3.5 3.5 7.5-7.5" fill="none" stroke="#fff" stroke-width="2.6"/></svg>A learning and training plan will be presented based on your<br>requirements.</li>
    <li><svg class="tick" viewBox="0 0 24 24" aria-hidden="true"><circle cx="12" cy="12" r="12" fill="var(--cyan-tick)"/><path d="M6.5 12.5l3.5 3.5 7.5-7.5" fill="none" stroke="#fff" stroke-width="2.6"/></svg>An appraisal update on your new skills.</li>
  </ul>

  <section class="contact">
    <h2 class="contact-title">Contact Info:</h2>
    <p class="contact-line">0161 4972015</p>
    <p class="contact-line">07700 918342</p>
    <p class="contact-line">grenwick@vellumail.net</p>
  </section>
</main>
</body>
</html>
```